Harbor Tap & Grille Menu Makeover

I am looking for a professional look to update our current menu. We are an independently owned sports bar and grill. Up to this point, I have done all of my own graphic designing. I am looking for something classy/family oriented. We are a very family friendly sports bar that offers a wide variety of menu options. Our website is www.harbortapgrille.example. This may help you get more of a feel for what type of place we are and what we offer. Our menu is listed on the website. My current menu is 8.5x14 inserts that feature a cover page, 4 inside pages and a back page. I would like something a little more condensed than this. Possibly a large tri-fold menu? I am open to all new ideas. I do have some pictures on my menu now, and would like to continue using a few pictures to feature some of my items. I would like something that is in a format that gives me the option to change items and prices on my own in the future. I would also like it to feature, or inform my patrons about our technology that we offer. We offer online ordering and we are a "verified venue" with Brewlogr.( a social site for craft beer lovers).

Industry/Entity Type

Sports Bar

Requirements
Nice to have
• Nice to have some pictures, but does not have to. We do feature 9 different beers on tap. A lot of them are local craft beers from the state of Kansas. Not sure if that is something we can feature, but it is a nice talking point. All of our tables and bar are hand built. With a rich mahogany finish on all of our woodwork, some type of "woodgrain" look into the menu would be nice.

```html
<!DOCTYPE html>
<html lang="en">
<head>
<meta charset="utf-8">
<title>Harbor Tap &amp; Grille — Appetizers</title>
<link href="https://fonts.googleapis.com/css2?family=Cinzel:wght@400;600;700&family=Oswald:wght@300;400&family=Montserrat:wght@600;700&display=swap" rel="stylesheet">
<style>
  :root{
    --wood-dark:#4a1d0b;
    --wood-mid:#7a3317;
    --wood-light:#9a4822;
    --paper-light:#e2cfa8;
    --paper-mid:#cfb384;
    --paper-edge:#a9834c;
    --ink:#1f140c;
    --white:#ffffff;
  }
  *{margin:0;padding:0;box-sizing:border-box}
  html,body{width:850px;height:1200px;overflow:hidden}
  body{
    position:relative;
    background:
      repeating-linear-gradient(90deg, rgba(0,0,0,.10) 0 2px, transparent 2px 37px, rgba(255,255,255,.04) 37px 40px, transparent 40px 85px),
      linear-gradient(90deg, var(--wood-dark) 0%, var(--wood-mid) 20%, var(--wood-light) 45%, var(--wood-mid) 70%, var(--wood-dark) 100%);
    font-family:'Oswald',sans-serif;
    color:var(--ink);
  }
  .brand{position:absolute;left:0;top:38px;width:850px;text-align:center;color:var(--ink)}
  .brand-rule{position:absolute;height:2px;background:var(--ink)}
  .brand-rule::before,.brand-rule::after{content:"";position:absolute;top:-2px;width:6px;height:6px;border-radius:50%;background:var(--ink)}
  .brand-rule::before{left:-6px}
  .brand-rule::after{right:-6px}
  .brand-rule--top{left:258px;top:17px;width:334px}
  .brand-rule--bottom{left:320px;top:105px;width:212px}
  .brand-name{position:absolute;left:0;top:24px;width:850px;font-family:'Cinzel',serif;font-weight:700;font-size:38px;letter-spacing:12px;line-height:1}
  .brand-sub{position:absolute;left:0;top:73px;width:850px;font-family:'Cinzel',serif;font-weight:700;font-size:17px;letter-spacing:1px;line-height:1}

  .parchment{position:absolute;left:44px;top:180px;width:760px;height:940px}

  .menu-title{position:absolute;left:0;top:250px;width:850px;text-align:center;font-family:'Cinzel',serif;font-weight:600;font-size:35px;line-height:1;letter-spacing:.5px}

  .item{position:absolute;left:262px;width:326px;text-align:center;text-transform:uppercase}
  .item-name{font-weight:400;font-size:15px;line-height:16px;letter-spacing:-.3px}
  .item-desc{font-weight:300;font-size:10.2px;line-height:12px;letter-spacing:-.35px}
  .item-price{font-family:'Montserrat',sans-serif;font-weight:700;font-size:7px;line-height:8px;letter-spacing:.5px}

  .feature-photo{position:absolute;left:580px;top:596px;width:156px;height:156px;border-radius:50%;
    border:2px solid var(--ink);
    background:radial-gradient(circle at 50% 45%, #f3eee0 0 10%, #c9a64a 22%, #a9963b 45%, #4f6b2a 62%, #111 80%)}

  .contact{position:absolute;left:0;top:1046px;width:850px;height:18px;display:flex;justify-content:center;gap:34px;font-family:'Montserrat',sans-serif;font-weight:700;font-size:8.5px;letter-spacing:1.1px;text-transform:uppercase;white-space:nowrap}
  .contact-item{display:flex;align-items:center;gap:12px;height:18px}
  .contact-mark{width:18px;height:18px;background:var(--ink);flex:none}

  .footnote{position:absolute;left:0;top:1152px;width:850px;text-align:center;color:var(--white);font-family:'Montserrat',sans-serif;font-weight:700;font-size:6.5px;letter-spacing:.6px;text-transform:uppercase}
</style>
</head>
<body>

<header class="brand">
  <div class="brand-rule brand-rule--top"></div>
  <h1 class="brand-name">HARBOR</h1>
  <p class="brand-sub">Tap &amp; Grille</p>
  <div class="brand-rule brand-rule--bottom"></div>
</header>

<svg class="parchment" viewBox="0 0 760 940" aria-hidden="true">
  <defs>
    <radialGradient id="paperTone" cx="50%" cy="45%" r="65%">
      <stop offset="0" stop-color="#e2cfa8"/>
      <stop offset=".65" stop-color="#cfb384"/>
      <stop offset="1" stop-color="#a9834c"/>
    </radialGradient>
  </defs>
  <polygon fill="url(#paperTone)" points="
    40,26 70,14 120,20 180,6 240,16 300,10 380,22 440,12 500,18 560,6 620,14 690,4 720,30 750,60 742,120 756,180
    744,260 752,330 740,400 756,470 744,540 752,620 738,700 750,780 736,850 746,900 700,930 640,920 580,936 520,924
    460,936 390,926 330,938 260,924 200,934 140,926 80,936 30,918 20,860 10,800 24,720 8,640 22,560 6,480
    20,400 4,320 18,240 6,160 22,80"/>
</svg>

<h2 class="menu-title">APPETIZERS</h2>

<div class="item" style="top:297px">
  <h3 class="item-name">Slider Burgers</h3>
  <p class="item-desc">Six juicy bite sized burgers topped with American cheese and served with pickle slices.</p>
  <p class="item-price">8.99</p>
</div>
<div class="item" style="top:353px">
  <h3 class="item-name">Loaded Potato Skins</h3>
  <p class="item-desc">Six crispy skins loaded with jack, cheddar and mozzarella cheese, then topped with smoked bacon and green onions. Served with sour cream.</p>
  <p class="item-price">8.99</p>
</div>
<div class="item" style="top:409px">
  <h3 class="item-name">Rattlesnake Eggs</h3>
  <p class="item-desc">A spicy combo of pepper jack cheese and jalapeños, battered and fried.</p>
  <p class="item-price">7.99</p>
</div>
<div class="item" style="top:453px">
  <h3 class="item-name">Mozzarella Cheese Sticks</h3>
  <p class="item-desc">Classic battered mozzarella cheese sticks served with ranch dressing.</p>
  <p class="item-price">7.99</p>
</div>
<div class="item" style="top:497px">
  <h3 class="item-name">Grand Slam French Fries</h3>
  <p class="item-desc">French fries loaded with jack, cheddar, mozzarella, bacon, jalapeños and green onions! Served with ranch dressing.</p>
  <p class="item-price">7.99</p>
</div>
<div class="item" style="top:553px">
  <h3 class="item-name">Bang Bang Shrimp</h3>
  <p class="item-desc">Lightly breaded and fried shrimp coated with a spicy Thai sauce, topped with Parmesan cheese and diced tomatoes. Served over a bed of romaine lettuce.</p>
  <p class="item-price">7.99</p>
</div>
<div class="item" style="top:609px">
  <h3 class="item-name">Ballpark Pretzel Basket</h3>
  <p class="item-desc">Buttered and salted pretzels served with nacho cheese sauce.</p>
  <p class="item-price">7.99</p>
</div>
<div class="item" style="top:653px">
  <h3 class="item-name">Spicy Southwest<br>Chicken Eggrolls</h3>
  <p class="item-desc">Stuffed with black beans, corn and chicken.<br>Served with southwest ranch.</p>
  <p class="item-price">9.99</p>
</div>
<div class="item" style="top:725px">
  <h3 class="item-name">Blooming Onion</h3>
  <p class="item-desc">This fan favorite is classically carved and deep fried to perfection. Served with Harbor signature dipping sauce.</p>
  <p class="item-price">7.99</p>
</div>
<div class="item" style="top:781px">
  <h3 class="item-name">Chicken Quesadilla</h3>
  <p class="item-desc">A 12 inch flour tortilla stuffed with grilled chicken and jack and cheddar cheese. Served with salsa.</p>
  <p class="item-price">8.99</p>
</div>
<div class="item" style="top:837px">
  <h3 class="item-name">Hank's Boneless Buffalo Wings</h3>
  <p class="item-desc">A full pound of spicy, boneless buffalo wings. Served with ranch dressing or Hank's Gold Label sauce.</p>
  <p class="item-price">7.99</p>
</div>
<div class="item" style="top:893px">
  <h3 class="item-name">Harbor Loaded Nachos</h3>
  <p class="item-desc">Tri-colored tortilla chips smothered with creamy Monterey jack cheese, choice of beef or chicken, and topped with grilled peppers and onions, jalapeños and diced tomatoes. Served with sour cream and salsa.</p>
  <p class="item-price">9.99</p>
</div>
<div class="item" style="top:961px">
  <h3 class="item-name">Garlic Bread Basket</h3>
  <p class="item-desc">Tri-colored tortilla chips smothered with creamy Monterey jack cheese, choice of beef or chicken, and topped with grilled peppers and onions, jalapeños and diced tomatoes. Served with sour cream and salsa.</p>
  <p class="item-price">9.99</p>
</div>

<div class="feature-photo" role="img" aria-label="Photo of spicy southwest chicken eggrolls arranged around a cup of ranch dip"></div>

<footer class="contact">
  <div class="contact-item"><span class="contact-mark"></span><span>harbortapgrille</span></div>
  <div class="contact-item"><span class="contact-mark"></span><span>harbortapgrille.example</span></div>
  <div class="contact-item"><span class="contact-mark"></span><span>Brewlogr</span></div>
</footer>

<p class="footnote">When splitting a large portion, you will be charged the price of a small portion if a small portion is offered</p>

</body>
</html>
```